Brindlewave.com website design

I need a basic website for www.brindlewave.com. Brindle Wave has been hosting websites since 2002 via partnership arrangement with Tessloft.com and Namequill.com. We do not do any design, only hosting for small companies and nonprofits. We are referring people to ArtHarbor and others to get their websites developed. Our website and pricing does not change often, but I need to be able to easily update the pricing and contact page.

Target Market(s)

Small company and non profit organizations

Industry/Entity Type

Utility

Coding

Coded - Design and coding required

Number of Pages Required

5+ page

Colors

Designer to choose colors to be used in the design.

Requirements
Must have
• Wordsmith format for easy content management. The logo attached. Contact us page with the following: Phone and fax are the same number: 877.514.2938. Email address is mybrindlewave@quorvix.com. Mailing address is 4816 E. Millhaven Rd #137, Kestrel Bend, AR 72908.
Nice to have
• Some kind of badge or tag line on the home page that celebrates our 15th year of hosting without a single hosting without any downtime. We are are 15 year partners with Tessloft.com and Namequill.com. Website Design tab needs to reference ArtHarbor or others for all their website design needs. We provide no design or updating services. We will provide the developers FTP access to our dedicated Linux server. We do not provide email services other than redirects to their proprietary email or gmail, yahoo, etc. Needs a services and pricing tab. We provide domain registration services via our partnership with Namequill.com. We will want a way for them to submit a suggested domain name for us to verify if available. I might be able to get a link from Namequill.com to our account for you to include on that tab REGISTER DOMAIN. The tab buttons can be: WHO WE ARE, WHAT WE DO, WHEN YOU NEED US, WHERE TO REACH US. Maybe consider making the WHO, WHAT, WHEN and WHERE a dark blue color the rest of the text different color just so they stand out
Should not have
• A lot of animation that takes a long time to open. Clean and simple website.

```html
<!DOCTYPE html>
<html lang="en">
<head>
<meta charset="utf-8">
<title>Brindle Wave – Website Hosting</title>
<link href="https://fonts.googleapis.com/css2?family=Open+Sans:wght@400;600;700;800&display=swap" rel="stylesheet">
<style>
:root{
  --navy:#0b3d6b;
  --navy-deep:#0a3560;
  --blue:#3a8fd0;
  --sky:#5fb3ea;
  --panel:#f2f2f2;
  --bar:#f4f4f4;
  --text:#666;
  --muted:#777;
  --white:#fff;
}
*{margin:0;padding:0;box-sizing:border-box}
html,body{width:902px;height:1200px;overflow:hidden;background:var(--white)}
body{font-family:"Open Sans",Arial,sans-serif;color:var(--text);position:relative}
.container{position:absolute;left:99px;width:704px}

.topbar{position:absolute;top:0;left:0;width:902px;height:30px;background:var(--bar)}
.topbar .container{height:30px;display:flex;justify-content:space-between;align-items:center;font-size:9.6px;color:var(--muted)}
.topbar span{display:flex;align-items:center;gap:4px;white-space:nowrap}
.topbar svg{width:8px;height:8px;fill:var(--muted)}

.header{position:absolute;top:30px;left:0;width:902px;height:122px}
.brand{position:absolute;left:99px;top:36px;display:flex;align-items:center;gap:8px}
.brand-mark{width:22px;height:22px;background:var(--blue)}
.brand-name{font-size:17px;font-weight:700;color:var(--navy);letter-spacing:.5px}
.auth{position:absolute;right:99px;top:32px;display:flex;gap:7px}
.btn-auth{height:28px;width:67px;display:flex;align-items:center;justify-content:center;gap:4px;font-size:10px;color:var(--white)}
.btn-auth svg{width:8px;height:8px;fill:var(--white)}
.btn-login{background:var(--sky)}
.btn-register{background:var(--navy)}
.nav{position:absolute;right:99px;top:76px;display:flex;gap:23px;font-size:10.4px;color:var(--muted)}

.hero{position:absolute;top:152px;left:0;width:902px;height:310px}
.hero-photo{position:absolute;inset:0;background:linear-gradient(115deg,#0a1c2c 0%,#1b5d7c 30%,#4d7c96 50%,#6a7fa5 72%,#6b4f9c 100%)}
.hero-title{position:absolute;top:130px;width:100%;text-align:center;color:var(--white);font-weight:800;font-size:24px;line-height:25px;text-shadow:0 1px 3px rgba(0,0,0,.5)}
.hero-arrow{position:absolute;top:144px;width:21px;height:22px;background:rgba(40,40,40,.7);display:flex;align-items:center;justify-content:center}
.hero-arrow svg{width:9px;height:9px;fill:#ccc}
.hero-arrow.prev{left:0}
.hero-arrow.next{right:0}

.feature{position:absolute;left:0;width:902px;height:240px;background:var(--panel)}
.feature-photo{position:absolute;top:0;width:451px;height:240px}
.who{top:462px}
.who .feature-photo{left:0;background:linear-gradient(90deg,#9fb3c6 0%,#dfe9f2 40%,#eef3f8 60%,#b9c8d6 100%)}
.what{top:702px}
.what .feature-photo{right:0;background:linear-gradient(135deg,#1e2a3c 0%,#4d6d90 45%,#8ea9c6 65%,#26354a 100%)}
.feature-copy{position:absolute;top:32px;width:328px}
.who .feature-copy{left:474px}
.what .feature-copy{left:100px}
.feature-title{font-size:26px;font-weight:800;letter-spacing:.3px;line-height:32px}
.who .feature-title{color:var(--blue)}
.what .feature-title{color:var(--navy)}
.feature-text{margin-top:10px;font-size:7.7px;line-height:14.4px;text-align:justify;color:var(--text)}
.btn-outline{margin-top:13px;display:inline-flex;align-items:center;justify-content:center;width:67px;height:28px;border:1px solid #c5c5c5;font-size:8.4px;color:var(--muted)}

.cta{position:absolute;top:942px;left:0;width:902px;height:174px;text-align:center}
.cta-line{margin-top:56px;font-size:19px;color:#333}
.btn-contact{margin-top:8px;display:inline-flex;align-items:center;justify-content:center;width:66px;height:27px;background:var(--navy);color:var(--white);font-size:9.6px}

.footer{position:absolute;top:1116px;left:0;width:902px;height:84px;background:var(--navy-deep)}
.footer-links{position:absolute;left:100px;top:23px;font-size:8.8px;color:#c8d3df;display:flex;gap:8px}
.copyright{position:absolute;left:100px;top:44px;font-size:8.8px;color:#c8d3df}
.social{position:absolute;right:99px;top:32px;display:flex;gap:6px}
.social span{width:19px;height:19px;border-radius:50%;background:#3e6fb0}
</style>
</head>
<body>

<div class="topbar">
  <div class="container">
    <span><svg viewBox="0 0 8 8"><rect x="2" y="0" width="4" height="8" rx="1"/></svg>Phone : 877.514.2938</span>
    <span><svg viewBox="0 0 8 8"><rect x="0" y="1.5" width="8" height="5"/></svg>Email : mybrindlewave@quorvix.com</span>
    <span><svg viewBox="0 0 8 8"><path d="M4 0a3 3 0 0 1 3 3c0 2-3 5-3 5S1 5 1 3a3 3 0 0 1 3-3z"/></svg>Mailing address is 4816 E. Millhaven Rd #137, Kestrel Bend, AR 72908.</span>
  </div>
</div>

<header class="header">
  <div class="brand"><span class="brand-mark"></span><span class="brand-name">BRINDLE WAVE</span></div>
  <div class="auth">
    <span class="btn-auth btn-login"><svg viewBox="0 0 8 8"><path d="M0 3h4V1l3 3-3 3V5H0z"/></svg>Log in</span>
    <span class="btn-auth btn-register"><svg viewBox="0 0 8 8"><path d="M0 8V6l5-5 2 2-5 5z"/></svg>Register</span>
  </div>
  <nav class="nav">
    <span>Home</span><span>Who we are</span><span>What we do</span><span>When you need us</span><span>Where to reach us</span>
  </nav>
</header>

<section class="hero">
  <div class="hero-photo" role="img" aria-label="Close-up of server rack hardware in blue and purple light"></div>
  <h1 class="hero-title">15TH YEAR OF HOSTING WITHOUT<br>A SINGLE HOSTING WITHOUT ANY DOWNTIME</h1>
  <span class="hero-arrow prev"><svg viewBox="0 0 10 10"><path d="M5 1 1 5l4 4V6h4V4H5z"/></svg></span>
  <span class="hero-arrow next"><svg viewBox="0 0 10 10"><path d="M5 1l4 4-4 4V6H1V4h4z"/></svg></span>
</section>

<section class="feature who">
  <div class="feature-photo" role="img" aria-label="Bright data center aisle lined with server cabinets"></div>
  <div class="feature-copy">
    <h2 class="feature-title">WHO WE ARE</h2>
    <p class="feature-text">Nam fermentum nibh eu euismod blandit. Sed tincidunt ipsum enim, vitae finibus arcu mollis sit amet. Ut interdum viverra dignissim. Interdum et malesuada fames ac ante ipsum primis in faucibus. Donec porta neque sit amet ante rutrum viverra. Mauris accumsan, libero nec semper scelerisque, justo enim porttitor mauris, a tincidunt nisl nulla volutpat nunc. Sed eu aliquet magna, et sollicitudin risus. Sed aliquet magna sit amet felis suscipit, id rhoncus nulla vehicula. Fusce dapibus lectus quam, non blandit augue vulputate vitae. Mauris pulvinar, odio sit amet lacinia cursus, ex metus</p>
    <span class="btn-outline">Read more</span>
  </div>
</section>

<section class="feature what">
  <div class="feature-copy">
    <h2 class="feature-title">WHAT WE DO</h2>
    <p class="feature-text">Nam fermentum nibh eu euismod blandit. Sed tincidunt ipsum enim, vitae finibus arcu mollis sit amet. Ut interdum viverra dignissim. Interdum et malesuada fames ac ante ipsum primis in faucibus. Donec porta neque sit amet ante rutrum viverra. Mauris accumsan, libero nec semper scelerisque, justo enim porttitor mauris, a tincidunt nisl nulla volutpat nunc. Sed eu aliquet magna, et sollicitudin risus. Sed aliquet magna sit amet felis suscipit, id rhoncus nulla vehicula. Fusce dapibus lectus quam, non blandit augue vulputate vitae. Mauris pulvinar, odio sit amet lacinia cursus, ex metus</p>
    <span class="btn-outline">Read more</span>
  </div>
  <div class="feature-photo" role="img" aria-label="Rack-mounted server units viewed at an angle"></div>
</section>

<section class="cta">
  <p class="cta-line">Interdum et malesuada fames ac ante ipsum primis in faucibus</p>
  <span class="btn-contact">Contact Us</span>
</section>

<footer class="footer">
  <div class="footer-links"><span>Home</span><span>|</span><span>Who we are</span><span>|</span><span>What we do</span><span>|</span><span>When you need us</span><span>|</span><span>Where to reach us</span></div>
  <p class="copyright">Copyright &copy; 2017 Company name, &nbsp;All rights rese4rved.</p>
  <div class="social" aria-label="Social links"><span></span><span></span><span></span></div>
</footer>

</body>
</html>
```